Bully breed rescue website

I need a website for my bully breed rescue. We rescue bully breeds from up and down the east coast of the United States and train them as service dogs for people with limited mobility disabilities. I don't want a lot of white space. I want it to be modern and slick and colorful and still look professional. I want it to be different and have a lot of wow factor. I linked a copy of my logo.

Number of Pages Required

5+ page

Font styles to use
Sans Serif

Colors

Designer to choose colors to be used in the design.

Requirements
Must have
• Moving aspects. Blog and ecommerce.
• 1.) Home page
• 2.) Services- something modular
• 3.) About US
• 4.) Blog
• 5.) Application page
• 6.) Donation page
• 7.) Contact Us
Nice to have
• Large Slider of photos on home page
• vertical menu bar
Should not have
• Lots of white space. Dont want it to look like a template or any other site

```html
<!DOCTYPE html>
<html lang="en">
<head>
<meta charset="utf-8">
<title>Steadfast Paws — Bully Breed Rescue</title>
<link rel="stylesheet" href="https://fonts.googleapis.com/css2?family=Dosis:wght@400;500;600;700&family=Raleway:wght@400;500;600&family=Roboto+Slab:wght@400&display=swap">
<style>
:root{
  --red:#c8202f;
  --wine:#8e1f2b;
  --wine-dark:#6a1520;
  --yellow:#f7c600;
  --navy:#1c1b36;
  --navy-card:#29284a;
  --ink:#333;
  --muted:#8a8a8a;
  --paper:#ffffff;
  --hero-bg:#f6f6f7;
}
*{box-sizing:border-box;margin:0;padding:0}
html,body{width:1200px;height:3158px;overflow:hidden}
body{position:relative;background:var(--paper);font-family:"Dosis",sans-serif;color:var(--ink)}
section,header,footer{position:absolute;left:0;width:1200px}
.btn{display:inline-flex;align-items:center;gap:6px;background:var(--yellow);color:var(--wine-dark);font:600 12px "Dosis",sans-serif;letter-spacing:.5px;text-transform:uppercase;height:32px;padding:0 32px}
.btn svg{width:10px;height:10px}
.section-title{text-align:center;font:500 32px "Dosis",sans-serif;letter-spacing:1px;text-transform:uppercase}

/* hero */
.hero{top:0;height:550px;background:var(--hero-bg)}
.menu-toggle{position:absolute;left:86px;top:16px;width:44px;height:44px}
.brand{position:absolute;left:450px;top:14px;width:300px;height:110px;display:flex;align-items:center;justify-content:center;gap:12px}
.brand-dot{width:18px;height:18px;border-radius:50%;background:var(--red)}
.brand-name{font:700 34px "Dosis",sans-serif;color:var(--ink);letter-spacing:.5px}
.hero-title{position:absolute;left:86px;top:248px;font:400 41px/52px "Roboto Slab",serif;color:var(--red);letter-spacing:1.5px;text-transform:uppercase}
.hero-lede{position:absolute;left:86px;top:356px;width:440px;font:600 16px/24px "Dosis",sans-serif;color:#3a3a3a}
.hero-circle{position:absolute;left:722px;top:166px;width:356px;height:356px;border-radius:50%;background:var(--yellow)}
.hero-dog{position:absolute;left:640px;top:196px;width:420px;height:270px;border-radius:40% 40% 30% 30%;background:radial-gradient(ellipse at 50% 45%,#f1e9df 0%,#c99a6c 60%,rgba(201,154,108,0) 72%)}

/* about */
.about{top:550px;height:440px;background:linear-gradient(90deg,#b5683f 0%,#8e2a2f 35%,#7d1e2a 100%)}
.about-photo{position:absolute;left:0;top:0;width:470px;height:440px;background:linear-gradient(120deg,#d89a5c 0%,#a65a35 55%,rgba(142,42,47,0) 100%)}
.about-frame{position:absolute;left:66px;top:42px;width:430px;height:338px;border:1px solid rgba(255,255,255,.75)}
.about-body{position:absolute;left:525px;top:34px;width:590px;color:#fff}
.about-body h2{font:500 30px "Dosis",sans-serif;text-transform:uppercase;letter-spacing:.5px;padding-bottom:6px;border-bottom:1px solid var(--yellow);width:500px}
.about-body p{font:400 13.5px/27px "Dosis",sans-serif;margin-top:14px;color:#f3e3e3}
.about .btn{position:absolute;left:525px;top:364px}

/* services */
.services{top:990px;height:410px;background:var(--paper)}
.services .section-title{position:absolute;top:38px;width:100%;color:#444}
.service-cards{position:absolute;left:86px;top:164px;display:flex;gap:23px}
.service-card{position:relative;width:247px;height:116px;background:#fff;box-shadow:0 2px 10px rgba(0,0,0,.12);display:flex;align-items:flex-end;justify-content:center;padding-bottom:26px;font:500 14px "Dosis",sans-serif;text-transform:uppercase;color:#333}
.service-icon{position:absolute;left:50%;top:-52px;margin-left:-42px;width:84px;height:84px}
.services .btn{position:absolute;left:525px;top:332px}

/* testimonials */
.testimonials{top:1400px;height:512px;background:linear-gradient(180deg,#9a3a42 0%,#8c2a35 100%)}
.testimonials .section-title{position:absolute;top:38px;width:100%;color:#fff}
.quotes{position:absolute;left:86px;top:114px;display:flex;gap:27px}
.quote{width:326px;text-align:center}
.quote-box{position:relative;height:190px;background:rgba(255,255,255,.18);border-top:4px solid rgba(255,255,255,.25);padding:34px 32px 0;font:400 13.5px/24px "Dosis",sans-serif;color:#fff}
.quote.active .quote-box{border-top-color:var(--yellow)}
.quote-box:after{content:"";position:absolute;left:50%;bottom:-12px;margin-left:-12px;border:12px solid transparent;border-bottom:0;border-top-color:rgba(255,255,255,.18)}
.avatar{width:68px;height:68px;border-radius:50%;background:linear-gradient(135deg,#e7c8a8,#a8745c);border:3px solid rgba(255,255,255,.6);margin:40px auto 0}
.quote-name{margin-top:12px;font:400 13px "Dosis",sans-serif;color:#fff}
.dots{position:absolute;left:0;width:100%;top:460px;display:flex;justify-content:center;gap:10px}
.dots span{width:8px;height:8px;border-radius:50%;background:rgba(255,255,255,.45)}
.dots span.on{background:#fff}

/* blog */
.blog{top:1912px;height:568px;background:var(--paper)}
.blog .section-title{position:absolute;top:40px;width:100%;color:#444}
.posts{position:absolute;left:86px;top:110px;display:flex;gap:27px}
.post{width:326px;height:348px;background:#fff;box-shadow:0 1px 8px rgba(0,0,0,.1);position:relative}
.post-media{height:192px;position:relative}
.post-date{position:absolute;left:18px;top:14px;width:38px;text-align:center;color:#fff}
.post-date b{display:block;background:var(--navy);font:600 18px/28px "Dosis",sans-serif}
.post-date i{display:block;background:var(--red);font:normal 500 9px/14px "Raleway",sans-serif}
.post-body{padding:20px 24px}
.post-body h3{font:400 18px "Raleway",sans-serif;color:#333}
.post-body p{margin-top:12px;font:400 12px/18px "Raleway",sans-serif;color:var(--muted)}
.post-body a{display:block;margin-top:12px;font:400 12px "Raleway",sans-serif;color:var(--red);text-decoration:none}
.post.featured{background:var(--wine)}
.post.featured h3{color:var(--yellow)}
.post.featured p{color:#f1d0d3}
.post.featured a{color:var(--yellow)}
.blog .btn{position:absolute;left:525px;top:494px}

/* contact */
.contact{top:2480px;height:320px;background:linear-gradient(180deg,#b2363c 0%,#a8323a 100%)}
.contact .section-title{position:absolute;top:40px;width:100%;color:#fff}
.field{position:absolute;border-bottom:1px solid rgba(255,255,255,.7);font:500 10px "Dosis",sans-serif;color:#fff;text-transform:uppercase;letter-spacing:.5px}
.contact .btn{position:absolute;left:525px;top:248px}

/* footer */
.site-footer{top:2800px;height:320px;background:var(--navy);color:#fff}
.foot-col{position:absolute;top:28px}
.foot-col h4{font:700 13px "Dosis",sans-serif;text-transform:uppercase;letter-spacing:.5px;margin-bottom:16px}
.quick-links li{list-style:none;font:400 13px/31px "Dosis",sans-serif}
.recent li{list-style:none;display:flex;gap:18px;margin-bottom:18px}
.thumb{width:62px;height:58px;flex:none;background:linear-gradient(135deg,#6a8fb0,#c46a4e)}
.recent p{font:400 11px/15px "Dosis",sans-serif;width:210px}
.recent time{display:block;margin-top:4px;font:400 10px "Dosis",sans-serif;color:#7d7ca3}
.info{width:236px;background:var(--navy-card);display:flex;gap:22px;padding:14px 16px;margin-bottom:9px}
.info svg{width:20px;height:20px;flex:none}
.info small{display:block;font:400 10px "Dosis",sans-serif;color:#d8d8e8}
.info span{display:block;margin-top:6px;font:400 11px/15px "Dosis",sans-serif}
.info .link{color:#e04b56}
.copyright{position:absolute;top:3120px;left:0;width:1200px;height:38px;background:var(--red);text-align:center;font:400 10px/38px "Dosis",sans-serif;color:#fff}
</style>
</head>
<body>

<header class="hero">
  <svg class="menu-toggle" viewBox="0 0 44 44" aria-label="Menu"><circle cx="22" cy="22" r="19" fill="none" stroke="#c8202f" stroke-width="3"/><path d="M13 15h18M13 22h18M13 29h18" stroke="#c8202f" stroke-width="3"/></svg>
  <div class="brand"><span class="brand-dot"></span><span class="brand-name">Steadfast Paws</span></div>
  <h1 class="hero-title">Saving dogs so<br>they can save us</h1>
  <p class="hero-lede">Lorem Ipsum is simply dummy text of the printing and typesetting industry. Lorem Ipsum has been</p>
  <div class="hero-circle"></div>
  <div class="hero-dog" role="img" aria-label="Photo of a bulldog lying down"></div>
</header>

<section class="about">
  <div class="about-photo" role="img" aria-label="Photo of a bulldog in an autumn field"></div>
  <div class="about-frame"></div>
  <div class="about-body">
    <h2>About Us</h2>
    <p>Lorem Ipsum is simply dummy text of the printing and typesetting industry. Lorem Ipsum has been the industry's standard dummy text ever since the 1500s, when an unknown printer took a galley of type and scrambled it to. Lorem Ipsum is simply dummy text of the printing and typesetting industry. Lorem Ipsum has been the industry's standard dummy text ever since the 1500s, when an unknown printer took a galley of type and scrambled it to Lorem Ipsum is simply dummy text of the printing and typesetting industry. Lorem Ipsum has been the industry's standard dummy text ever since the 1500s, when an unknown printer took a galley of type and scrambled it to Lorem Ipsum is simply dummy text of the printing and typesetting industry.</p>
  </div>
  <span class="btn">Read more <svg viewBox="0 0 10 10"><path d="M2 1l5 4-5 4z" fill="currentColor"/></svg></span>
</section>

<section class="services">
  <h2 class="section-title">Services</h2>
  <div class="service-cards">
    <div class="service-card"><svg class="service-icon" viewBox="0 0 84 84"><rect x="18" y="18" width="48" height="48" transform="rotate(45 42 42)" fill="#f7c600"/><path d="M30 48h24l-3 6H33z M36 44v-8h12v8" fill="none" stroke="#fff" stroke-width="2"/></svg>Lorem ipsum is simply</div>
    <div class="service-card"><svg class="service-icon" viewBox="0 0 84 84"><rect x="18" y="18" width="48" height="48" transform="rotate(45 42 42)" fill="#f7c600"/><rect x="30" y="34" width="24" height="18" rx="2" fill="none" stroke="#fff" stroke-width="2"/><circle cx="42" cy="43" r="5" fill="none" stroke="#fff" stroke-width="2"/></svg>Lorem ipsum is simply</div>
    <div class="service-card"><svg class="service-icon" viewBox="0 0 84 84"><rect x="18" y="18" width="48" height="48" transform="rotate(45 42 42)" fill="#f7c600"/><circle cx="42" cy="42" r="11" fill="none" stroke="#fff" stroke-width="2"/><path d="M37 42l4 4 7-8" fill="none" stroke="#fff" stroke-width="2"/></svg>Lorem ipsum is simply</div>
    <div class="service-card"><svg class="service-icon" viewBox="0 0 84 84"><rect x="18" y="18" width="48" height="48" transform="rotate(45 42 42)" fill="#f7c600"/><circle cx="36" cy="36" r="4" fill="#fff"/><circle cx="48" cy="36" r="4" fill="#fff"/><ellipse cx="42" cy="49" rx="8" ry="6" fill="#fff"/></svg>Lorem ipsum is simply</div>
  </div>
  <span class="btn">View more <svg viewBox="0 0 10 10"><path d="M2 1l5 4-5 4z" fill="currentColor"/></svg></span>
</section>

<section class="testimonials" role="img" aria-label="Background photo of a person with a service dog" style="background:linear-gradient(180deg,#9a3a42 0%,#8c2a35 100%)">
  <h2 class="section-title">Testimonials</h2>
  <div class="quotes">
    <div class="quote"><div class="quote-box">" Lorem Ipsum is simply dummy text of the printing and typesetting industry. Lorem Ipsum has been the industry's standard dummy text ever since the 1500s, when an unknown printer took a galley of</div><div class="avatar" role="img" aria-label="Portrait of the reviewer"></div><div class="quote-name">Jane Doe</div></div>
    <div class="quote active"><div class="quote-box">" Lorem Ipsum is simply dummy text of the printing and typesetting industry. Lorem Ipsum has been the industry's standard dummy text ever since the 1500s, when an unknown printer took a galley of "</div><div class="avatar" role="img" aria-label="Portrait of the reviewer"></div><div class="quote-name">John Doe</div></div>
    <div class="quote"><div class="quote-box">Is simply dummy text of the printing and typesetting industry. Lorem Ipsum has been the industry's standard dummy text ever since the 1500s, when an unknown printer took a galley of "</div><div class="avatar" role="img" aria-label="Portrait of the reviewer"></div><div class="quote-name">Jane Doe</div></div>
  </div>
  <div class="dots"><span></span><span class="on"></span><span></span></div>
</section>

<section class="blog">
  <h2 class="section-title">Blog</h2>
  <div class="posts">
    <article class="post">
      <div class="post-media" role="img" aria-label="Photo of a bulldog in a life vest swimming" style="background:linear-gradient(160deg,#cfe6f5,#5d9fd0 60%,#e38a2a)"><div class="post-date"><b>30</b><i>Sep</i></div></div>
      <div class="post-body"><h3>Lorem ipsum dolor sit amet</h3><p>Claritas est etiam processus dynamicus, qui sequitur mutationem consuetudium.</p><a>Read More ›</a></div>
    </article>
    <article class="post featured">
      <div class="post-media" role="img" aria-label="Photo of a dog on a forest path" style="background:linear-gradient(160deg,#3c4a3a,#6b5a3e 60%,#2e3a2c)"><div class="post-date"><b>30</b><i>Sep</i></div></div>
      <div class="post-body"><h3>Lorem ipsum dolor sit amet</h3><p>Claritas est etiam processus dynamicus, qui sequitur mutationem consuetudium.</p><a>Read More ›</a></div>
    </article>
    <article class="post">
      <div class="post-media" role="img" aria-label="Photo of a bulldog in a red coat in the snow" style="background:linear-gradient(160deg,#eef1f4,#d9cbbd 55%,#c83a3a)"><div class="post-date"><b>30</b><i>Sep</i></div></div>
      <div class="post-body"><h3>Lorem ipsum dolor sit amet</h3><p>Claritas est etiam processus dynamicus, qui sequitur mutationem consuetudium.</p><a>Read More ›</a></div>
    </article>
  </div>
  <span class="btn">View more <svg viewBox="0 0 10 10"><path d="M2 1l5 4-5 4z" fill="currentColor"/></svg></span>
</section>

<section class="contact" role="img" aria-label="Background photo of a hand holding a paw">
  <h2 class="section-title">Contact Us</h2>
  <div class="field" style="left:172px;top:102px;width:418px;height:18px">Name *</div>
  <div class="field" style="left:612px;top:102px;width:418px;height:18px">Email</div>
  <div class="field" style="left:172px;top:148px;width:858px;height:58px">Message</div>
  <span class="btn">Send message <svg viewBox="0 0 10 10"><path d="M2 1l5 4-5 4z" fill="currentColor"/></svg></span>
</section>

<footer class="site-footer">
  <div class="foot-col" style="left:86px">
    <h4>Quick Links</h4>
    <ul class="quick-links"><li>Home</li><li>Services</li><li>About US</li><li>Blog</li><li>Application page</li><li>Donation</li><li>Contact Us</li></ul>
  </div>
  <div class="foot-col" style="left:436px">
    <h4>Recent Posts</h4>
    <ul class="recent">
      <li><div class="thumb" role="img" aria-label="Blog post thumbnail"></div><p>Lorem Ipsum is simply dummy text of the printing and typesetting industry. Lorem<time>February 26, 2018</time></p></li>
      <li><div class="thumb" role="img" aria-label="Blog post thumbnail"></div><p>Lorem Ipsum is simply dummy text of<time>February 26, 2018</time></p></li>
      <li><div class="thumb" role="img" aria-label="Blog post thumbnail"></div><p>Lorem Ipsum is simply dummy text of the printing andstandard<time>February 26, 2018</time></p></li>
    </ul>
  </div>
  <div class="foot-col" style="left:876px">
    <h4>Contact Us</h4>
    <div class="info"><svg viewBox="0 0 20 20"><rect x="5" y="1" width="10" height="18" rx="2" fill="none" stroke="#fff" stroke-width="1.5"/><path d="M8 16h4" stroke="#fff"/></svg><div><small>Phone number</small><span style="font-size:15px">+00 . 0000 . 0000</span></div></div>
    <div class="info"><svg viewBox="0 0 20 20"><rect x="2" y="5" width="16" height="11" fill="none" stroke="#fff" stroke-width="1.5"/><path d="M2 5l8 6 8-6" fill="none" stroke="#fff" stroke-width="1.5"/></svg><div><small>Email Address</small><span class="link">hello@steadfastpaws.org</span></div></div>
    <div class="info"><svg viewBox="0 0 20 20"><path d="M10 18s-6-6-6-10a6 6 0 0112 0c0 4-6 10-6 10z" fill="none" stroke="#fff" stroke-width="1.5"/><circle cx="10" cy="8" r="2" fill="#fff"/></svg><div><small>Address</small><span>Lorem Ipsum is simply dummy text of the printing and typesetting industry. Lorem Ipsum has been</span></div></div>
  </div>
</footer>
<div class="copyright">© 2018 steadfast paws | all rights reserved</div>

</body>
</html>
```